Business card for Internet Marketing Consultant

Simple - need a nice business card design using the logo elements and colors. Keywords: Progressive, professional, stylish, minimalist. Please use the bc as part of the design.

Info for card:

Gareth Pennick
Internet Marketing Strategist
Phone: (520) 318-6047
Email: gareth@brightcanopy.com
Address: 2915 W. Larkmoor Ave., Ste. 118
Tucson, Arizona 85293

Website: www.brightcanopy.com

Industry/Entity Type

Business

Font styles to use
Sans Serif

```html
<!DOCTYPE html>
<html lang="en">
<head>
<meta charset="utf-8">
<title>Bright Canopy – Business Card</title>
<link href="https://fonts.googleapis.com/css2?family=Jost:wght@400;500;600&display=swap" rel="stylesheet">
<style>
  :root {
    --brand-blue: #2d5da5;
    --brand-green: #5fb06a;
    --ink-grey: #8a8d90;
    --paper: #ffffff;
    --backdrop: #e4e5e7;
  }
  * { box-sizing: border-box; margin: 0; padding: 0; }
  html, body {
    width: 1200px; height: 900px; overflow: hidden;
    background: var(--backdrop);
    font-family: "Jost", "Futura", sans-serif;
  }
  .stage { position: relative; width: 1200px; height: 900px; }
  .card {
    position: absolute; top: 152px;
    width: 340px; height: 596px;
    background: var(--paper);
    overflow: hidden;
    box-shadow: 0 6px 20px rgba(0,0,0,.12);
  }
  .card--front { left: 215px; }
  .card--back  { left: 645px; }

  /* front */
  .front-band {
    position: absolute; top: 0; left: 0; right: 0; height: 92px;
    background: var(--brand-green);
  }
  .front-brand {
    position: absolute; top: 150px; left: 0; right: 0; text-align: center;
  }
  .front-block {
    position: absolute; left: 0; right: 0; bottom: 0; height: 300px;
    background: var(--brand-blue);
  }

  /* shared brand lockup */
  .brand-name {
    font-weight: 600; font-size: 40px; letter-spacing: -0.5px;
    color: var(--brand-blue); line-height: 1;
  }
  .brand-tagline {
    margin-top: 6px;
    font-size: 11.5px; letter-spacing: 3.2px; text-transform: uppercase;
    color: var(--ink-grey);
  }

  /* back */
  .back-brand {
    position: absolute; top: 78px; left: 0; right: 0; text-align: center;
  }
  .back-brand .brand-mark {
    display: block; width: 18px; height: 18px; margin: 0 auto 16px;
    background: var(--brand-green);
  }
  .back-brand .brand-name { font-size: 34px; }
  .back-brand .brand-tagline { font-size: 10px; letter-spacing: 2.6px; }

  .accent-square {
    position: absolute; top: 262px; right: 14px;
    width: 18px; height: 18px; background: var(--brand-blue);
  }
  .name-band {
    position: absolute; top: 288px; left: 0; right: 14px; height: 62px;
    background: var(--brand-green);
    padding: 10px 0 0 50px;
    color: var(--paper);
  }
  .person-name { font-weight: 600; font-size: 16px; line-height: 1.2; }
  .person-title { font-size: 16px; line-height: 1.3; }

  .contact {
    position: absolute; top: 385px; left: 50px; right: 10px;
    list-style: none;
    font-size: 14px; color: var(--brand-blue); line-height: 1.35;
  }
  .contact li { display: flex; }
  .contact .label { width: 20px; flex: none; color: var(--brand-green); }
  .contact .gap { margin-top: 14px; }
</style>
</head>
<body>
<main class="stage">

  <section class="card card--front" aria-label="Card front">
    <div class="front-band"></div>
    <div class="front-brand">
      <div class="brand-name">brightcanopy</div>
      <div class="brand-tagline">Internet Marketing Strategies</div>
    </div>
    <div class="front-block"></div>
  </section>

  <section class="card card--back" aria-label="Card back">
    <div class="back-brand">
      <span class="brand-mark"></span>
      <div class="brand-name">brightcanopy</div>
      <div class="brand-tagline">Internet Marketing Strategies</div>
    </div>

    <div class="accent-square"></div>
    <div class="name-band">
      <div class="person-name">Gareth Pennick</div>
      <div class="person-title">Internet Marketing Strategist</div>
    </div>

    <ul class="contact">
      <li><span class="label">P</span><span>(520) 318-6047</span></li>
      <li><span class="label">E</span><span>gareth@brightcanopy.com</span></li>
      <li class="gap"><span class="label">A</span><span>2915 W. Larkmoor Ave., Ste. 118<br>Tucson, Arizona 85293</span></li>
      <li class="gap"><span class="label">W</span><span>www.brightcanopy.com</span></li>
    </ul>
  </section>

</main>
</body>
</html>
```